I need to refresh my meeting minutes pages (2 of them)

I have 2 pages that need to be modernized with a new look and feel. I have attached the 2 pages that need the refresh. I am okay with one page submissions as long as the winner is willing to add the second page before payment :-) Any questions please let me know. The logo on the page is not ours but a sample of what client may give us.

```html
<!DOCTYPE html>
<html lang="en">
<head>
<meta charset="utf-8">
<title>NVSD Meetings</title>
<link href="https://fonts.googleapis.com/css2?family=Mulish:wght@400;500;600;700;800&display=swap" rel="stylesheet">
<style>
:root{
  --green:#066b2e;
  --ink:#222;
  --band:#e9eaec;
  --panel-dark:#333333;
  --rule:#d4d4d4;
  --star-off:#b5b5b5;
}
*{box-sizing:border-box;margin:0;padding:0}
html,body{width:1200px;height:785px;overflow:hidden}
body{font-family:"Mulish",sans-serif;color:var(--ink);background:var(--band);position:relative}
.abs{position:absolute}

.site-header{position:absolute;left:0;top:0;width:1200px;height:97px;background:#fff;border-top:2px solid var(--green)}
.brand{position:absolute;left:44px;top:26px;font-size:34px;font-weight:700;color:var(--green);line-height:1}
.user-tab{position:absolute;left:880px;top:0;width:282px;height:34px}
.user-tab a{position:absolute;top:6px;color:#fff;font-size:12.5px;font-weight:600;display:flex;align-items:center;gap:5px;text-decoration:none}
.main-nav{position:absolute;top:54px;left:0;width:1200px;font-size:15px}
.main-nav span{position:absolute;color:var(--ink)}
.main-nav .active{color:var(--green);border-bottom:1px solid var(--green);padding-bottom:2px}

.search-band{position:absolute;left:0;top:97px;width:1200px;height:43px;background:var(--band);border-bottom:1px solid #dcdcdc}
.search-input{position:absolute;left:290px;top:5px;width:508px;height:32px;background:#fff;border:1px solid #d8d8d8;font-size:12px;color:#444;padding:7px 8px}
.search-input i{position:absolute;right:12px;top:9px;width:14px;height:14px;border:1.5px solid #888;border-radius:50%}
.search-btn{position:absolute;left:806px;top:6px;width:119px;height:31px;background:var(--green);color:#fff;font-size:14px;font-weight:600;text-align:center;line-height:31px}

.sidebar{position:absolute;left:40px;top:156px;width:339px;height:579px;background:var(--panel-dark)}
.sidebar .hello{position:absolute;left:16px;top:8px;color:#fff;font-size:16.5px;font-weight:700;display:flex;align-items:center;gap:4px}
.sidebar .inner{position:absolute;left:8px;top:40px;width:326px;height:532px;background:#fff}
.welcome{height:56px;background:var(--green);color:#fff;font-size:21px;font-weight:800;padding:14px 9px}
.acc-row{position:relative;height:50px;border-bottom:1px solid var(--rule);display:flex;align-items:center;padding-left:9px;gap:10px;font-size:18px;font-weight:500}
.acc-row .toggle{position:absolute;right:12px;font-size:20px;font-weight:700}
.year{border:none;color:var(--green);height:46px}
.meet-list{position:absolute;width:300px}
.meet{position:relative;height:45px;padding-left:67px;font-size:12.5px;line-height:19px}
.meet svg{position:absolute;left:44px;top:3px}
.meet.on{color:var(--green)}
.scroll-track{position:absolute;left:314px;top:188px;width:5px;height:366px;background:#eee}
.scroll-track i{position:absolute;left:0;top:0;width:5px;height:232px;background:#cfcfcf}

.pager{position:absolute;top:156px;width:29px;height:24px;display:flex;align-items:center;justify-content:center}
.pager.prev{left:401px;background:#2f2f2f}
.pager.next{left:432px;background:var(--green)}

.content{position:absolute;left:401px;top:188px;width:758px;height:505px;background:#fff;border:1px solid #dedede}
.content h1{position:absolute;left:23px;top:18px;font-size:17px;font-weight:500;color:var(--green)}
.content .date{position:absolute;left:24px;top:45px;font-size:14.5px}
.content hr{position:absolute;left:24px;width:712px;border:none;border-top:1px solid var(--rule)}
.venue{position:absolute;left:24px;top:91px;font-size:14.5px;color:var(--green);font-weight:500}
.addr{position:absolute;left:24px;top:119px;font-size:14.5px;line-height:23px}
.addr .line{display:flex;align-items:flex-start;gap:8px}
.addr .ind{padding-left:24px}
.desc{position:absolute;left:24px;top:206px;width:620px;font-size:14.5px;line-height:23px}
.actions{position:absolute;left:21px;top:449px;display:flex;gap:19px}
.action{width:157px;height:52px;border:1px solid #d0d0d0;background:#f7f7f7;display:flex;align-items:center;gap:9px;font-size:12.5px;line-height:15px;color:#333;white-space:nowrap}
</style>
</head>
<body>

<header class="site-header">
  <div class="brand">NVSD</div>
  <div class="user-tab">
    <svg class="abs" width="282" height="36" viewBox="0 0 282 36"><path d="M0 0 H282 Q262 0 250 20 Q238 36 220 36 H50 Q32 36 22 20 Q12 0 0 0 Z" fill="var(--green)"/><line x1="117" y1="7" x2="117" y2="26" stroke="#fff" stroke-opacity=".6"/></svg>
    <a style="left:32px"><svg width="13" height="14" viewBox="0 0 13 14"><rect x="1" y="1" width="8" height="12" fill="none" stroke="#fff" stroke-width="1.5"/><path d="M5 7 H12 M9.5 4.5 L12 7 L9.5 9.5" fill="none" stroke="#fff" stroke-width="1.5"/></svg>Sign Out</a>
    <a style="left:128px"><svg width="14" height="14" viewBox="0 0 14 14"><circle cx="7" cy="3.5" r="3" fill="#fff"/><path d="M1 14 V10 Q1 7 4 7 L7 10 L10 7 Q13 7 13 10 V14Z" fill="#fff"/></svg>Mark Ellison</a>
  </div>
  <nav class="main-nav">
    <span style="left:798px">Featured</span>
    <span class="active" style="left:904px">Meetings</span>
    <span style="left:1010px">Agenda</span>
    <span style="left:1109px">Policies</span>
  </nav>
</header>

<div class="search-band">
  <div class="search-input">search meetings<i></i></div>
  <div class="search-btn">Search</div>
</div>

<aside class="sidebar">
  <div class="hello"><svg width="20" height="22" viewBox="0 0 20 22"><circle cx="10" cy="5" r="4.5" fill="#fff"/><path d="M1 22 V15 Q1 10 6 10 L10 15 L14 10 Q19 10 19 15 V22Z" fill="#fff"/></svg>Hello Mark</div>
  <div class="inner">
    <div class="welcome">Welcome to NVSD</div>
    <div class="acc-row"><svg width="24" height="24" viewBox="0 0 24 24"><rect x="1" y="1" width="22" height="22" fill="none" stroke="#444"/><circle cx="12" cy="12" r="5" fill="none" stroke="#444" stroke-width="1.5" stroke-dasharray="2 1.3"/><circle cx="12" cy="12" r="2" fill="none" stroke="#444"/></svg>Featured<span class="toggle">+</span></div>
    <div class="acc-row year"><svg width="24" height="24" viewBox="0 0 24 24"><rect x="1" y="3" width="22" height="20" fill="none" stroke="var(--green)" stroke-width="1.5"/><line x1="1" y1="8" x2="23" y2="8" stroke="var(--green)"/><line x1="6" y1="1" x2="6" y2="5" stroke="var(--green)" stroke-width="1.5"/><line x1="18" y1="1" x2="18" y2="5" stroke="var(--green)" stroke-width="1.5"/><text x="12" y="18" font-size="6" text-anchor="middle" fill="var(--green)" font-family="Mulish">365</text></svg>2015<span class="toggle" style="top:8px">–</span></div>
  </div>
  <div class="meet-list" style="left:8px;top:187px">
    <div class="meet on"><svg width="14" height="13" viewBox="0 0 14 13"><path d="M7 0 L8.8 4.5 L14 5 L10 8.2 L11.3 13 L7 10.3 L2.7 13 L4 8.2 L0 5 L5.2 4.5Z" fill="var(--green)"/></svg>May 1, 2025 (Thu)<br>Special Meeting Agenda</div>
    <div class="meet"><svg width="14" height="13" viewBox="0 0 14 13"><path d="M7 0 L8.8 4.5 L14 5 L10 8.2 L11.3 13 L7 10.3 L2.7 13 L4 8.2 L0 5 L5.2 4.5Z" fill="var(--star-off)"/></svg>May 1, 2025 (Thu)<br>Special Meeting Agenda</div>
    <div class="meet"><svg width="14" height="13" viewBox="0 0 14 13"><path d="M7 0 L8.8 4.5 L14 5 L10 8.2 L11.3 13 L7 10.3 L2.7 13 L4 8.2 L0 5 L5.2 4.5Z" fill="var(--star-off)"/></svg>May 1, 2025 (Thu)<br>Special Meeting Agenda</div>
    <div class="meet"><svg width="14" height="13" viewBox="0 0 14 13"><path d="M7 0 L8.8 4.5 L14 5 L10 8.2 L11.3 13 L7 10.3 L2.7 13 L4 8.2 L0 5 L5.2 4.5Z" fill="var(--star-off)"/></svg>May 1, 2025 (Thu)<br>Special Meeting Agenda</div>
    <div class="meet"><svg width="14" height="13" viewBox="0 0 14 13"><path d="M7 0 L8.8 4.5 L14 5 L10 8.2 L11.3 13 L7 10.3 L2.7 13 L4 8.2 L0 5 L5.2 4.5Z" fill="var(--star-off)"/></svg>May 1, 2025 (Thu)<br>Special Meeting Agenda</div>
    <div class="meet"><svg width="14" height="13" viewBox="0 0 14 13"><path d="M7 0 L8.8 4.5 L14 5 L10 8.2 L11.3 13 L7 10.3 L2.7 13 L4 8.2 L0 5 L5.2 4.5Z" fill="var(--star-off)"/></svg>May 1, 2025 (Thu)<br>Special Meeting Agenda</div>
    <div class="meet"><svg width="14" height="13" viewBox="0 0 14 13"><path d="M7 0 L8.8 4.5 L14 5 L10 8.2 L11.3 13 L7 10.3 L2.7 13 L4 8.2 L0 5 L5.2 4.5Z" fill="var(--star-off)"/></svg>May 1, 2025 (Thu)<br>Special Meeting Agenda</div>
    <div class="meet"><svg width="14" height="13" viewBox="0 0 14 13"><path d="M7 0 L8.8 4.5 L14 5 L10 8.2 L11.3 13 L7 10.3 L2.7 13 L4 8.2 L0 5 L5.2 4.5Z" fill="var(--star-off)"/></svg>May 1, 2025 (Thu)<br>Special Meeting Agenda</div>
  </div>
  <div class="scroll-track"><i></i></div>
</aside>

<div class="pager prev"><svg width="10" height="14" viewBox="0 0 10 14"><path d="M8 1 L2 7 L8 13" fill="none" stroke="#fff" stroke-width="2.5"/></svg></div>
<div class="pager next"><svg width="10" height="14" viewBox="0 0 10 14"><path d="M2 1 L8 7 L2 13" fill="none" stroke="#fff" stroke-width="2.5"/></svg></div>

<main class="content">
  <h1>Regular Meeting Agenda</h1>
  <div class="date">Thursday, April 24, 2025</div>
  <hr style="top:77px">
  <div class="venue">Lakeview High School Media Center</div>
  <div class="addr">
    <div class="line"><svg width="16" height="20" viewBox="0 0 16 20"><path d="M8 19 Q1 11 1 7.5 A7 7 0 0 1 15 7.5 Q15 11 8 19Z" fill="none" stroke="#333" stroke-width="1.3"/><circle cx="8" cy="7.5" r="2.5" fill="none" stroke="#333" stroke-width="1.3"/></svg>1840 North Willow Creek Road</div>
    <div class="ind">Brookfield, Ohio 44210</div>
    <div class="line"><svg width="16" height="16" viewBox="0 0 16 16" style="margin-top:2px"><path d="M8 1.5 A6.5 6.5 0 1 1 2 5" fill="none" stroke="#333" stroke-width="1.3"/><path d="M8 4 V8 L11 10" fill="none" stroke="#333" stroke-width="1.3"/></svg>06:00 pm</div>
  </div>
  <hr style="top:197px">
  <p class="desc">This meeting is a meeting of the Board of Education in public for the purpose of conducting the District’s business. There is a time for public participation durin View the Agenda</p>
  <div class="actions">
    <div class="action" style="padding-left:25px;gap:7px"><svg width="32" height="40" viewBox="0 0 32 40"><path d="M1 1 H23 L31 9 V39 H1Z" fill="none" stroke="var(--green)" stroke-width="1.8"/><path d="M6 13 H26 M6 19 H26 M6 25 H26 M6 31 H26" stroke="var(--green)" stroke-width="1.6" stroke-dasharray="2 1.5 20 0"/></svg>View<br>the Agenda</div>
    <div class="action" style="padding-left:13px;gap:8px"><svg width="34" height="40" viewBox="0 0 34 40"><path d="M6 1 H25 L32 8 V39 H6Z" fill="none" stroke="var(--green)" stroke-width="1.8"/><rect x="1" y="14" width="28" height="14" fill="var(--green)"/><text x="15" y="25.5" font-size="12" font-weight="800" fill="#fff" text-anchor="middle" font-family="Mulish">PDF</text></svg>Download<br>Agenda as PDF</div>
    <div class="action" style="padding-left:19px;gap:12px"><svg width="38" height="36" viewBox="0 0 38 36"><rect x="9" y="1" width="20" height="10" fill="none" stroke="var(--green)" stroke-width="1.8"/><rect x="1" y="10" width="36" height="16" rx="2" fill="none" stroke="var(--green)" stroke-width="1.8"/><rect x="9" y="20" width="20" height="15" fill="#fff" stroke="var(--green)" stroke-width="1.8"/><path d="M13 25 H25 M13 29 H25" stroke="var(--green)" stroke-width="1.5"/></svg>Print<br>the Agenda</div>
    <div class="action" style="padding-left:28px;gap:9px"><svg width="40" height="38" viewBox="0 0 44 38"><circle cx="35" cy="7" r="6" fill="none" stroke="var(--green)" stroke-width="1.8"/><circle cx="8" cy="20" r="6" fill="none" stroke="var(--green)" stroke-width="1.8"/><circle cx="35" cy="31" r="6" fill="none" stroke="var(--green)" stroke-width="1.8"/><path d="M13 17 L30 9 M13 23 L30 28" stroke="var(--green)" stroke-width="1.8"/></svg>Share<br>this Page</div>
  </div>
</main>

<footer style="position:absolute;left:0;top:735px;width:1200px;height:50px;background:var(--green);color:#fff;text-align:center;font-size:17px;font-weight:600;line-height:50px">@ 2015 &nbsp;NVSD. All Rights Reserved</footer>

</body>
</html>
```